American Ingenuity + Italian Design = RTB
International consulting services from fine arts/advertising/construction & special events. A new company that will find the right connections to get your job done.

Card should include -
1. Company Name with logo: rosalind tavore Enterprises LLC
2. Address: 218 Dunmore Lane, Highland Springs, VA 23081
3. Phone Number: 804.512.3096 (US)
4. Tagline: American Ingenuity + Italian Style + RTB (you can improve on this idea)
5. web address to be added eventually

Likes: airplanes and boats to give the idea of movement & international ability
Logo: if you have an idea to adjust the colors, we are open to that. Rosalind likes blues, but other colors didn't seem to work; remember this will print 4c in most cases)
Updates

I have uploaded the logo on it's own. Typical business card size for the US is 3.5" x 2", but doesn't have to be that size. the flyer was just for reference of something else that was done and to give some background. I hope that didn't confuse anyone.

Thank you all for the amazing work in the tight deadline. We will be reviewing everything today and will provide feedback by tomorrow. I will also pass this site on to anyone I know looking for design work.

website address rosalindtavore.example email rosalind@rosalindtavore.example Italian number +39 347 861 2054 USA 1 804 512 3096 International Consulting Services American Ingenuity. Italian Design. rtB These are the vital elements for the card. In addition please note the new fotos should have been uploaded. Best Regards

Target Market(s)

Companies or individuals that want to bring the Italian flair to the US or American know how to Italian projects. This can range from a bride planning a destination wedding, an interior designer looking to add pieces or knowledge to their project, or an investor looking to buy property to invest and build.

Industry/Entity Type

Construction

Requirements
Must have
• 1. Company Name with logo: rosalind tavore Enterprises LLC
+39 347 861 2054 (Italia)
Nice to have
• incorporate the idea of international ability; airplanes (like the wing in the background of the logo)
Should not have
• not overly decorative

```html
<!DOCTYPE html>
<html lang="en">
<head>
<meta charset="utf-8">
<title>rosalind tavore Enterprises LLC — Business Card</title>
<link rel="stylesheet" href="https://fonts.googleapis.com/css2?family=Arimo:wght@400;700&family=Oswald:wght@300;400&display=swap">
<style>
  :root {
    --page: #d9d9d7;
    --card-back: #dcd8d5;
    --card-back-edge: #cfcac6;
    --photo-light: #e9e1db;
    --photo-mid: #cdbdb2;
    --photo-dark: #a8958a;
    --brand-red: #8e2b22;
    --ink: #1b1b1b;
    --faint: rgba(142, 43, 34, 0.10);
  }
  * { box-sizing: border-box; margin: 0; padding: 0; }
  html, body {
    width: 1200px; height: 1200px; overflow: hidden;
    background: var(--page);
  }
  .sheet {
    position: relative; width: 1200px; height: 1200px;
    display: flex; flex-direction: column; align-items: center; justify-content: center;
    gap: 70px;
  }
  .card {
    position: relative; width: 770px; height: 440px; overflow: hidden;
    box-shadow: 0 6px 18px rgba(0,0,0,0.18);
  }

  /* Front */
  .card-front { background: var(--photo-light); }
  .front-photo {
    position: absolute; inset: 0;
    background:
      linear-gradient(118deg, transparent 0%, transparent 48%, rgba(255,255,255,0.35) 56%, transparent 66%),
      linear-gradient(160deg, var(--photo-light) 0%, var(--photo-mid) 60%, var(--photo-dark) 100%);
  }
  .front-brand {
    position: absolute; left: 0; right: 0; top: 0; bottom: 0;
    display: flex; align-items: center; justify-content: center; gap: 16px;
    padding-top: 40px;
  }
  .brand-dot {
    flex: none;
    width: 26px; height: 26px; border-radius: 50%;
    background: var(--brand-red);
  }
  .brand-name {
    font-family: "Arimo", Arial, sans-serif; font-weight: 700;
    color: var(--brand-red); font-size: 40px; white-space: nowrap;
  }

  /* Back */
  .card-back {
    background: linear-gradient(180deg, var(--card-back) 0%, var(--card-back-edge) 100%);
    display: flex; flex-direction: column; align-items: center;
    padding-top: 72px;
  }
  .back-faint {
    position: absolute; left: 0; right: 0; bottom: 62px;
    text-align: center;
    font-family: "Arimo", Arial, sans-serif; font-weight: 700;
    font-size: 40px; color: var(--faint); white-space: nowrap;
  }
  .back-brand {
    position: relative; display: flex; align-items: center; gap: 12px;
    margin-bottom: 28px;
  }
  .back-brand .brand-name { font-size: 28px; }
  .back-brand .brand-dot { width: 18px; height: 18px; }
  .details {
    position: relative; text-align: center; color: var(--ink);
    font-family: "Arimo", Arial, sans-serif; font-size: 21px; line-height: 1.3;
  }
  .details .contact {
    font-family: "Oswald", "Arial Narrow", sans-serif; font-weight: 300;
    font-size: 22px;
  }
</style>
</head>
<body>
<main class="sheet">
  <section class="card card-front" aria-label="Business card front">
    <div class="front-photo" role="img" aria-label="Soft sepia photograph of an airplane wing over the sea"></div>
    <div class="front-brand">
      <span class="brand-dot"></span>
      <span class="brand-name">rosalind tavore Enterprises LLC</span>
    </div>
  </section>

  <section class="card card-back" aria-label="Business card back">
    <div class="back-faint" aria-hidden="true">rosalind tavore Enterprises LLC</div>
    <div class="back-brand">
      <span class="brand-dot"></span>
      <span class="brand-name">rosalind tavore Enterprises LLC</span>
    </div>
    <div class="details">
      <p>International Consulting Services</p>
      <p>American Ingenuity. Italian Design. rtB</p>
      <p class="contact">(website) rosalindtavore.example &amp; (email) rosalind@rosalindtavore.example</p>
      <p class="contact">(Italian) +39 347 861 2054 / (USA) 1 804 512 3096</p>
    </div>
  </section>
</main>
</body>
</html>
```